Website needed for modern mobile app developer for small business'

Hi

We are looking for someone to design a very modern looking website with company logo that outlines what our business is and let's users purchase a mobile app designed by our company. (For ideas think buildora.io or ) The user should be able to describe what functionality they require and we will go and provide a test version of their app built

We would also like a testimonials page.

I currently have hosting on Kelvane Hosting, so if this could be taken into account that would be great.
Updates

here is the logo - if colour scheme could match that would be great Added Wednesday, March 30, 2016

Target Market(s)

Small and medium business

Industry/Entity Type

Business

Number of Pages Required

3 page

Requirements
Must have
• Homepage who we are and what we offer
• Pricing page explaining the different products available - HTML5 app, Android App or iPhone app with an option to purchase
• A testimonials page
• A one that makes it easier for potential customers to get in contact.

```html
<!DOCTYPE html>
<html lang="en">
<head>
<meta charset="utf-8">
<title>Company — Mobile App Builder</title>
<link href="https://fonts.googleapis.com/css2?family=Open+Sans:wght@300;400;600;700&display=swap" rel="stylesheet">
<style>
:root{
  --teal:#1b8fa3;
  --teal-light:#2bb3c0;
  --salmon:#f47a7a;
  --ink:#222831;
  --muted:#6b7076;
  --paper:#ffffff;
  --page-bg:#eef0f2;
  --who-bg:#a9d2d2;
  --offer-dark:#24282d;
  --footer:#25282d;
  --customer:#2a9d98;
  --red-badge:#d9401e;
  --cyan-badge:#2fc0c0;
  --blue-badge:#5e8fc9;
  --orange-badge:#f5932a;
}
*{margin:0;padding:0;box-sizing:border-box}
html,body{width:1200px;height:3214px;overflow:hidden}
body{font-family:'Open Sans',Arial,sans-serif;background:var(--page-bg);color:var(--ink);position:relative}
.abs{position:absolute}

/* Hero */
.hero{left:0;top:0;width:1200px;height:561px;overflow:hidden}
.hero-photo{position:absolute;inset:0;background:linear-gradient(100deg,#4a4341 0%,#6d615b 35%,#9b8e86 60%,#d9d5d2 100%)}
.hero-phone{left:620px;top:100px;width:300px;height:460px;border-radius:40px;background:linear-gradient(160deg,#2c2c30,#121214)}
.brand-mark{left:143px;top:30px;width:63px;height:63px;border:3px solid #fff;background:rgba(255,255,255,.15)}
.brand-word{left:143px;top:96px;width:70px;color:#fff;font-size:12px;letter-spacing:1px}
.topline{left:246px;top:60px;width:840px;height:1px;background:rgba(255,255,255,.6)}
.login{left:909px;top:19px;width:83px;height:28px;border:1px solid #fff;color:#fff;font-size:14px;text-align:center;line-height:26px}
.top-link{top:21px;color:#fff;font-size:14px}
.nav a{position:absolute;top:68px;color:#fff;font-size:15px;text-decoration:none}
.hero-title{left:143px;top:152px;width:460px;color:#fff;font-weight:300;font-size:40px;line-height:48px}
.hero-sub{left:143px;top:288px;width:250px;color:#fff;font-size:19px;line-height:27px}
.btn-outline{left:146px;top:403px;width:169px;height:38px;border:2px solid #fff;color:#fff;font-size:20px;text-align:center;line-height:34px}
.arrow{top:259px;width:40px;height:40px;border:2px solid #fff;border-radius:50%}

/* Section headings */
.heading{width:1200px;left:0;text-align:center;font-size:34px;font-weight:400}
.heading-bar{left:540px;width:120px;height:4px;background:var(--teal-light)}

/* Build */
.build{left:0;top:561px;width:1200px;height:607px;background:#f3f4f5}
.plan{top:669px;width:392px;height:467px;background:var(--paper);box-shadow:0 4px 14px rgba(0,0,0,.18)}
.plan-top{position:absolute;left:0;top:0;width:392px;height:215px}
.plan-title{position:absolute;left:0;width:392px;text-align:center;color:#fff;font-weight:700;font-size:34px;line-height:44px}
.plan-text{position:absolute;top:263px;left:20px;width:352px;text-align:center;color:var(--muted);font-size:16px;line-height:25px}
.plan-price{position:absolute;top:325px;width:392px;text-align:center;font-size:36px;font-weight:600}
.plan-price span{font-size:22px;vertical-align:4px}
.plan-btn{position:absolute;top:394px;left:91px;width:210px;height:48px;color:#fff;text-align:center;line-height:48px;font-weight:600;font-size:17px}

/* Who we are */
.who{left:0;top:1168px;width:1200px;height:392px;background:linear-gradient(90deg,#c9e3e2,var(--who-bg) 60%,#9ccaca)}
.who-title{left:124px;top:1222px;font-size:27px;color:#143b4d}
.who-bar{left:124px;top:1268px;width:160px;height:2px;background:#143b4d}
.who-text{left:124px;top:1280px;width:380px;font-size:17px;line-height:28px;color:#1d3d48}
.who-list{left:124px;top:1388px;font-size:13px;color:#1d3d48}
.who-list li{list-style:none;height:35px;display:flex;align-items:center;gap:10px}
.who-art{left:548px;top:1185px;width:540px;height:365px;border-radius:12px;background:radial-gradient(circle at 50% 50%,#e5eeef 0,#c5dfdf 60%,transparent 75%)}

/* Stats */
.stats{left:0;top:1560px;width:1200px;height:257px;background:linear-gradient(#e8e9ea,#ffffff)}
.stat{top:1588px;width:200px;text-align:center}
.stat-badge{width:108px;height:108px;border-radius:50%;margin:0 auto;display:flex;align-items:center;justify-content:center}
.stat-num{margin-top:12px;font-size:21px;color:var(--muted)}
.stat-label{margin-top:10px;font-size:17px;font-weight:700}

/* Offer */
.offer{left:0;top:1817px;width:1200px;height:590px;background:linear-gradient(90deg,#dce8ee 0%,#8f9ba3 30%,#3a4046 55%,var(--offer-dark) 100%)}
.tablet{left:161px;top:1918px;width:358px;height:454px;border-radius:22px;background:#1a1a1c;box-shadow:0 8px 20px rgba(0,0,0,.35)}
.tablet-screen{position:absolute;left:36px;top:38px;width:286px;height:372px;background:linear-gradient(#7c6d66 0,#7c6d66 26%,#f1f1f1 26%,#f1f1f1 70%,#a9d2d2 70%)}
.offer-title{left:590px;top:1858px;color:#fff;font-size:34px}
.offer-bar{left:590px;top:1907px;width:130px;height:4px;background:var(--teal-light)}
.offer-intro{left:592px;top:1923px;width:460px;color:#fff;font-size:16px;line-height:21px}
.offer-item{left:580px;width:500px;display:flex;align-items:center;gap:34px;color:#fff;font-size:16px;line-height:20px}
.offer-item p{width:390px}

/* Testimonial */
.testimonial{left:0;top:2407px;width:1200px;height:557px;background:#f3f4f5}
.testi-lead{left:0;top:2497px;width:1200px;text-align:center;font-size:14px}
.avatar{border-radius:50%;background:radial-gradient(circle at 50% 40%,#c9a98e 0,#8a5b45 55%,#3b2620 100%)}
.avatar-main{border:6px solid #ffffff;box-shadow:0 0 0 3px #8b2f2a}
.testi-name{left:0;top:2732px;width:1179px;text-align:center;font-size:17px}
.dot{top:2784px;width:80px;height:5px;background:#8a8d90}
.dot.active{background:var(--teal-light)}

/* Customers */
.customers{left:195px;top:2812px;width:810px;height:173px;background:var(--customer);z-index:2}
.customers h2{position:absolute;top:8px;width:810px;text-align:center;color:#fff;font-weight:400;font-size:34px}
.customers .bar{position:absolute;left:335px;top:62px;width:140px;height:3px;background:#fff}
.client{position:absolute;top:94px;width:128px;height:51px;background:#fff;color:#3c4045;font-size:16px;font-weight:600;display:flex;align-items:center;justify-content:center}

/* Footer */
.footer{left:0;top:2964px;width:1200px;height:250px;background:linear-gradient(90deg,#2c3036,var(--footer) 50%,#3b3f45)}
.foot-col{top:3008px;font-size:14px;color:#fff;line-height:27px}
.foot-col h3{color:var(--teal-light);font-weight:400;font-size:17px;margin-bottom:4px}
.foot-mark{left:955px;top:3010px;width:52px;height:52px;border:3px solid #fff}
.foot-word{left:952px;top:3064px;color:#fff;font-size:11px;letter-spacing:1px}
.social{top:3099px;width:28px;height:28px;border-radius:50%;background:#5d6167}
.social.first{background:var(--teal-light)}
.foot-rule{left:0;top:3182px;width:1200px;height:1px;background:#44484e}
.copyright{left:0;top:3188px;width:1200px;text-align:center;color:#fff;font-size:12px}
</style>
</head>
<body>

<!-- Hero -->
<section class="hero abs">
  <div class="hero-photo" role="img" aria-label="Photo of a hand holding a smartphone showing app icons, warm blurred interior behind"></div>
  <div class="hero-phone abs" role="img" aria-label="Smartphone with app icon grid on screen"></div>
  <div class="brand-mark abs"></div>
  <div class="brand-word abs">COMPANY</div>
  <div class="login abs">Log In</div>
  <div class="top-link abs" style="left:1011px">Building</div>
  <div class="topline abs"></div>
  <nav class="nav">
    <a href="#" style="left:688px">Home</a>
    <a href="#" style="left:783px">Services</a>
    <a href="#" style="left:893px">About Us</a>
    <a href="#" style="left:1010px">Pricing</a>
  </nav>
  <h1 class="hero-title abs">Lorem ipsum dolor sit amet</h1>
  <p class="hero-sub abs">In et nibh leo. Etiam tincidunt malesuada libero.</p>
  <div class="btn-outline abs">SIGN UP</div>
  <svg class="arrow abs" style="left:55px" viewBox="0 0 40 40"><path d="M23 12l-8 8 8 8" stroke="#fff" stroke-width="2.5" fill="none"/></svg>
  <svg class="arrow abs" style="left:1103px;border:none;background:#fff" viewBox="0 0 40 40"><path d="M17 12l8 8-8 8" stroke="#555" stroke-width="2.5" fill="none"/></svg>
</section>

<!-- What do you want to build -->
<section class="build abs"></section>
<h2 class="heading abs" style="top:582px">What do You Want to Build</h2>
<div class="heading-bar abs" style="top:640px"></div>

<article class="plan abs" style="left:195px">
  <div class="plan-top" role="img" aria-label="Soft pink photo of a laptop on a desk" style="background:linear-gradient(160deg,#f6b0a8,#e9868a)"></div>
  <svg class="abs" style="left:0;top:150px" width="392" height="80" viewBox="0 0 392 80"><path d="M0 40 Q196 110 392 30 L392 80 L0 80Z" fill="#fff"/><path d="M0 40 Q196 110 392 30" stroke="#f05a5a" stroke-width="6" fill="none"/></svg>
  <div class="plan-title" style="top:90px">A Mobile Site</div>
  <p class="plan-text">Maecenas tempor sollicitudin magna. Mauris consequat congue suscipit.</p>
  <div class="plan-price"><span style="color:var(--salmon)">$</span>3000</div>
  <div class="plan-btn" style="background:var(--salmon)">VIEW</div>
</article>

<article class="plan abs" style="left:613px">
  <div class="plan-top" role="img" aria-label="Soft blue photo of a hand using a phone" style="background:linear-gradient(160deg,#a8d8ee,#4aa8d6)"></div>
  <svg class="abs" style="left:0;top:150px" width="392" height="80" viewBox="0 0 392 80"><path d="M0 40 Q196 110 392 30 L392 80 L0 80Z" fill="#fff"/><path d="M0 40 Q196 110 392 30" stroke="#1b8fc0" stroke-width="6" fill="none"/></svg>
  <div class="plan-title" style="top:70px">A professional<br>Native App</div>
  <p class="plan-text">Maecenas tempor sollicitudin magna. Mauris consequat congue suscipit.</p>
  <div class="plan-price"><span style="color:var(--teal)">$</span>3000</div>
  <div class="plan-btn" style="background:var(--teal)">VIEW</div>
</article>

<!-- Who we are -->
<section class="who abs"></section>
<h2 class="who-title abs" style="font-weight:400">Who we are</h2>
<div class="who-bar abs"></div>
<p class="who-text abs">Donec tincidunt, orci ut vestibulum congue, quam odio bibendum turpis, vitae scelerisque metus arcu ac diam.</p>
<ul class="who-list abs">
  <li><svg width="18" height="18" viewBox="0 0 18 18"><circle cx="9" cy="9" r="7.5" stroke="#1d3d48" fill="none"/><path d="M5.5 9.2l2.4 2.4 4.6-5" stroke="#1d3d48" stroke-width="1.5" fill="none"/></svg>Free Domain Name</li>
  <li><svg width="18" height="18" viewBox="0 0 18 18"><circle cx="9" cy="9" r="7.5" stroke="#1d3d48" fill="none"/><path d="M5.5 9.2l2.4 2.4 4.6-5" stroke="#1d3d48" stroke-width="1.5" fill="none"/></svg>Flexible Panel</li>
  <li><svg width="18" height="18" viewBox="0 0 18 18"><circle cx="9" cy="9" r="7.5" stroke="#1d3d48" fill="none"/><path d="M5.5 9.2l2.4 2.4 4.6-5" stroke="#1d3d48" stroke-width="1.5" fill="none"/></svg>Regular Updates</li>
</ul>
<div class="who-art abs" role="img" aria-label="Flat illustration of cloud, devices, storage and office icons connected by dashed lines"></div>

<!-- Stats -->
<section class="stats abs"></section>
<div class="stat abs" style="left:134px">
  <div class="stat-badge" style="background:var(--red-badge)"><svg width="50" height="44" viewBox="0 0 50 44" fill="#fff"><circle cx="25" cy="9" r="7"/><rect x="17" y="18" width="16" height="22" rx="4"/><circle cx="9" cy="13" r="5"/><rect x="3" y="20" width="12" height="16" rx="3"/><circle cx="41" cy="13" r="5"/><rect x="35" y="20" width="12" height="16" rx="3"/></svg></div>
  <div class="stat-num">4,256</div><div class="stat-label">Customer</div>
</div>
<div class="stat abs" style="left:393px">
  <div class="stat-badge" style="background:var(--cyan-badge)"><svg width="50" height="50" viewBox="0 0 50 50"><circle cx="25" cy="22" r="14" fill="#fff"/><path d="M25 14l2.6 5.3 5.8.8-4.2 4.1 1 5.8-5.2-2.7-5.2 2.7 1-5.8-4.2-4.1 5.8-.8z" fill="var(--cyan-badge)"/><path d="M8 30q4 12 14 14M42 30q-4 12-14 14" stroke="#fff" stroke-width="3" fill="none"/></svg></div>
  <div class="stat-num">642</div><div class="stat-label">Award winner</div>
</div>
<div class="stat abs" style="left:622px">
  <div class="stat-badge" style="background:var(--blue-badge)"><svg width="40" height="50" viewBox="0 0 40 50"><circle cx="20" cy="22" r="11" stroke="#fff" stroke-width="3" fill="none"/><rect x="15" y="35" width="10" height="7" fill="#fff"/><path d="M20 2v5M4 10l4 3M36 10l-4 3M2 24h5M38 24h-5" stroke="#fff" stroke-width="2.5"/></svg></div>
  <div class="stat-num">12</div><div class="stat-label">Hours worked</div>
</div>
<div class="stat abs" style="left:864px">
  <div class="stat-badge" style="background:var(--orange-badge)"><svg width="50" height="44" viewBox="0 0 50 44" fill="#fff"><rect x="13" y="2" width="24" height="10"/><rect x="3" y="14" width="44" height="18" rx="3"/><rect x="13" y="26" width="24" height="16" stroke="var(--orange-badge)" stroke-width="2"/></svg></div>
  <div class="stat-num">50</div><div class="stat-label">Completed project</div>
</div>

<!-- What we offer -->
<section class="offer abs" role="img" aria-label="Blurred photo of a hand holding a phone over a dark doodle background"></section>
<div class="tablet abs"><div class="tablet-screen" role="img" aria-label="Website preview shown on the tablet screen"></div></div>
<h2 class="offer-title abs" style="font-weight:400">What we Offer</h2>
<div class="offer-bar abs"></div>
<p class="offer-intro abs">Maecenas tempor sollicitudin magna. Mauris consequat congue suscipit.</p>
<div class="offer-item abs" style="top:2013px"><svg width="52" height="52" viewBox="0 0 52 52" fill="none" stroke="#2bb3c0" stroke-width="2"><path d="M10 26a16 16 0 0 1 28-10M42 26a16 16 0 0 1-28 10"/><path d="M38 8v8h-8M14 44v-8h8"/></svg><p>Maecenas tempor sollicitudin magna. Mauris consequat congue suscipit.</p></div>
<div class="offer-item abs" style="top:2103px"><svg width="52" height="52" viewBox="0 0 52 52" fill="none" stroke="#2bb3c0" stroke-width="2"><rect x="8" y="6" width="28" height="40" rx="3"/><circle cx="36" cy="34" r="10"/></svg><p>Maecenas tempor sollicitudin magna. Mauris consequat congue suscipit.</p></div>
<div class="offer-item abs" style="top:2193px"><svg width="52" height="52" viewBox="0 0 52 52" fill="none" stroke="#2bb3c0" stroke-width="2"><rect x="10" y="10" width="18" height="34" rx="2"/><path d="M15 4h8v6"/><circle cx="36" cy="36" r="8"/></svg><p>Maecenas tempor sollicitudin magna. Mauris consequat congue suscipit.</p></div>
<div class="offer-item abs" style="top:2283px"><svg width="52" height="52" viewBox="0 0 52 52" fill="none" stroke="#2bb3c0" stroke-width="2"><path d="M14 6h24M14 46h24M16 6q0 14 10 20q10-6 10-20M16 46q0-14 10-20q10 6 10 20"/></svg><p>Maecenas tempor sollicitudin magna. Mauris consequat congue suscipit.</p></div>

<!-- Testimonial -->
<section class="testimonial abs"></section>
<h2 class="heading abs" style="top:2430px">Testimonial</h2>
<div class="heading-bar abs" style="top:2483px"></div>
<p class="testi-lead abs">Lorem ipsum dolor sit amet, consectetur adipiscing elit. Ut ornare, eros viverra ullamcorper gravida.</p>
<div class="avatar abs" role="img" aria-label="Portrait photo of a client" style="left:291px;top:2578px;width:116px;height:116px"></div>
<div class="avatar avatar-main abs" role="img" aria-label="Portrait photo of Marisa Holt" style="left:503px;top:2550px;width:172px;height:172px"></div>
<div class="avatar abs" role="img" aria-label="Portrait photo of a client" style="left:782px;top:2578px;width:116px;height:116px"></div>
<div class="testi-name abs">Marisa Holt</div>
<div class="dot active abs" style="left:455px"></div>
<div class="dot abs" style="left:548px"></div>
<div class="dot abs" style="left:641px"></div>

<!-- Customers -->
<section class="customers abs">
  <h2>Customer</h2>
  <div class="bar"></div>
  <div class="client" style="left:40px">Corvane</div>
  <div class="client" style="left:193px">Tallowby</div>
  <div class="client" style="left:343px">Brenwick Funds</div>
  <div class="client" style="left:493px">Quarro</div>
  <div class="client" style="left:643px">Halden Optic</div>
</section>

<!-- Footer -->
<footer class="footer abs"></footer>
<div class="foot-col abs" style="left:129px"><h3>Support</h3>Knowledge center<br>Devloper center<br>Support home</div>
<div class="foot-col abs" style="left:373px"><h3>Company</h3>Contact us<br>Privacy policy<br>Terms &amp; condition<br>Site map</div>
<div class="foot-col abs" style="left:620px"><h3>Product</h3>Pro<br>Business<br>Enterprise<br>Mailbox</div>
<div class="foot-mark abs"></div>
<div class="foot-word abs">COMPANY</div>
<div class="social first abs" style="left:897px"></div>
<div class="social abs" style="left:934px"></div>
<div class="social abs" style="left:971px"></div>
<div class="social abs" style="left:1008px"></div>
<div class="social abs" style="left:1045px"></div>
<div class="foot-rule abs"></div>
<div class="copyright abs">© 2016. newapp.example All rights reserved</div>

</body>
</html>
```